Bramble Café retail envelop design

This is a single serve coffee product for the adventurer consumer. The product is Fair Trade, Organic coffee grounds in a single serve pouch that can be used as a quality pour over drip brew while on the go. We would like to use designs that show adventure/hiking/camping with earth tones that display a organic/biodegradable feel.The open width of envelope film is 200mmThe finished bag size is W 100mm * L 120mm. (Once sealed)The eye mark size is W 10* H 5 mm. (side seam)Top/Bottom heat seal: 8mmSide heat seal: 7mmPlease use the samples provided as a guide only. I would like to see what you can come up with. Please use our original logo attached.Three blend varieties: Kelvermoor, Hollow, WarsawIG: @Bramblecafe

Target Market(s)

Adventurers, backpackers, campers, hikers, adventure riders, etc.

Colors

Designer to choose colors to be used in the design.

Requirements
Must have
• My Bramble Cafe logo, earthy feel (maybe black logo on earthy paper color backdrop?). Must show 12g size, instruction panel (this can be edited for visual appeal), IG account: Bramblecafe.
• Design will be printed in Matte finish.
Should not have
• It does not need all of the text that is shown on the back. I will prefer a more simplistic design rather than a crowded one.

```html
<!DOCTYPE html>
<html lang="en">
<head>
<meta charset="utf-8">
<title>Bramble Café – Single Serve Pouch</title>
<link rel="stylesheet" href="https://fonts.googleapis.com/css2?family=Oswald:wght@500;600&family=Yellowtail&family=Roboto:wght@400&display=swap">
<style>
  :root {
    --page: #ffffff;
    --ember: #e4532a;
    --ember-deep: #c8441f;
    --kraft: #c49a6c;
    --kraft-deep: #a97f55;
    --seal: #b88c5e;
    --stripe: #f4f4f4;
    --ink: #3a2417;
    --badge-ink: #1d1d1d;
    --ridge: #9c7049;
  }
  * { margin: 0; padding: 0; box-sizing: border-box; }
  html, body { width: 1200px; height: 1190px; overflow: hidden; background: var(--page); }
  .canvas { position: relative; width: 1200px; height: 1190px; }

  .pouch {
    position: absolute; left: 290px; top: 170px; width: 620px; height: 850px;
    border-radius: 10px; overflow: hidden; background: var(--kraft);
  }
  .pouch__top {
    position: absolute; left: 0; top: 0; width: 100%; height: 246px;
    background: linear-gradient(90deg, var(--ember), var(--ember-deep) 50%, var(--ember));
  }
  .pouch__zip {
    position: absolute; left: 40px; right: 40px; top: 92px; height: 14px;
    border-top: 2px solid rgba(0,0,0,.12); border-bottom: 2px solid rgba(0,0,0,.12);
  }
  .pouch__stripe {
    position: absolute; left: 0; top: 246px; width: 100%; height: 32px; background: var(--stripe);
  }
  .pouch__body {
    position: absolute; left: 0; top: 278px; width: 100%; bottom: 0;
    background: linear-gradient(90deg, var(--kraft-deep), var(--kraft) 30%, var(--kraft) 70%, var(--kraft-deep));
  }
  .pouch__seal {
    position: absolute; inset: 0; border: 26px solid transparent;
    box-shadow: inset 0 0 0 2px rgba(0,0,0,.08);
    pointer-events: none; border-radius: 10px;
  }
  .pouch__seal--top { position: absolute; left: 0; right: 0; top: 26px; height: 2px; background: rgba(0,0,0,.1); }
  .pouch__seal--bottom { position: absolute; left: 0; right: 0; bottom: 26px; height: 2px; background: rgba(0,0,0,.1); }

  .badge {
    position: absolute; left: 202px; top: 152px; width: 216px; height: 216px;
    border-radius: 50%; background: #fff; border: 6px solid #fff;
    box-shadow: inset 0 0 0 4px var(--badge-ink);
    display: flex; align-items: center; justify-content: center;
  }
  .badge__name {
    font-family: "Oswald", sans-serif; font-weight: 600; font-size: 34px; line-height: 1.05;
    color: var(--badge-ink); text-align: center; letter-spacing: 1px;
  }

  .title {
    position: absolute; left: 0; width: 100%; top: 400px; text-align: center;
    font-family: "Yellowtail", cursive; font-size: 70px; color: var(--ink); line-height: 1;
  }
  .subtitle {
    position: absolute; left: 0; width: 100%; top: 490px; text-align: center;
    font-family: "Oswald", sans-serif; font-weight: 500; font-size: 25px; letter-spacing: 1px;
    color: var(--ink); text-transform: uppercase;
  }
  .blend {
    position: absolute; left: 0; width: 100%; top: 528px; text-align: center;
    font-family: "Yellowtail", cursive; font-size: 92px; color: var(--ember); line-height: 1;
  }
  .range {
    position: absolute; left: 0; width: 100%; top: 630px; height: 196px;
    background: linear-gradient(180deg, rgba(156,112,73,0) 0%, rgba(156,112,73,.55) 40%, rgba(156,112,73,.25) 100%);
  }
  .weight {
    position: absolute; left: 535px; top: 754px; width: 74px; height: 74px; border-radius: 50%;
    background: #000; border: 3px solid #fff;
    display: flex; align-items: center; justify-content: center;
    font-family: "Roboto", sans-serif; font-size: 33px; color: #fff;
  }
</style>
</head>
<body>
<div class="canvas">
  <div class="pouch">
    <div class="pouch__top"><div class="pouch__zip"></div></div>
    <div class="pouch__stripe"></div>
    <div class="pouch__body"></div>
    <div class="range" role="img" aria-label="Illustration of a snowy mountain range in soft brown tones"></div>
    <div class="pouch__seal--top"></div>
    <div class="pouch__seal--bottom"></div>

    <div class="badge"><span class="badge__name">Bramble<br>Café</span></div>

    <div class="title">Quality Roast</div>
    <div class="subtitle">Single Serve</div>
    <div class="blend">Hollow</div>

    <div class="weight">12g</div>
  </div>
</div>
</body>
</html>
```